Football tournament flyer

I would like a quick turn around for this please.
I need a flyer to promote an 11 aside football tournament I am organising to celebrate the 23rd independence of my country Somaliland. Please use the national colours of our flag in the flyer, I have attached a file for your consideration.
The tournament will take place on 10/05/2014, from 9am - 8pm. The venue will be Corvell Open Space, Tresham Lane, Enfield, EN7 2QJ.
Refreshments, food and entertainment will be provided.
The name of the cup is Warsadeq Cup.
Spaces are limited and the entry fee per team is £200. All proceeds are for charity projects in Somaliland.
To register a team contact Bashir Yusuf on 07591 248 613 or Warsame Hirsi on 07462 571 380.
The best players will have the opportunity to represent Somaliland in an international game on the 17/05/2014.
The tournament is organised by Dalmar FC and Kindwell Foundation.
Industry/Entity Type
Entertainment

```html
<!DOCTYPE html>
<html lang="en">
<head>
<meta charset="utf-8">
<title>Warsadeq Cup – 11 Aside Football Tournament</title>
<link href="https://fonts.googleapis.com/css2?family=Kaushan+Script&family=Oswald:wght@700&family=Tinos:ital,wght@0,400;0,700;1,400;1,700&family=Nunito:wght@900&family=Arimo:wght@400;700&display=swap" rel="stylesheet">
<style>
  :root {
    --frame-black: #1a1a1a;
    --frame-line: #f4f4f4;
    --ink: #161616;
    --paper: #ffffff;
    --red: #e2352b;
    --green: #2f8a3c;
    --band: #1c1c1c;
  }
  html, body {
    margin: 0;
    padding: 0;
    overflow: hidden;
    background: var(--frame-black);
  }
  .flyer {
    position: relative;
    width: 935px;
    height: 1200px;
    overflow: hidden;
    background: var(--frame-black);
  }
  .panel {
    position: absolute;
    left: 27px;
    top: 30px;
    width: 878px;
    height: 1135px;
    border: 2px solid var(--frame-line);
    border-radius: 4px;
    overflow: hidden;
    background: var(--paper);
  }
  .art {
    position: absolute;
    inset: 0;
  }
  .headline {
    position: absolute;
    margin: 0;
    white-space: nowrap;
  }
  .celebrating {
    left: 48px;
    top: 50px;
    font-family: "Kaushan Script", cursive;
    font-size: 38px;
    color: var(--ink);
    transform: rotate(-2deg);
  }
  .celebrating .ordinal { color: var(--red); }
  .celebrating .occasion { font-family: "Tinos", serif; font-weight: 700; font-size: 36px; }
  .cup-name {
    left: 58px;
    top: 118px;
    font-family: "Oswald", sans-serif;
    font-size: 104px;
    line-height: 1;
    color: var(--red);
    -webkit-text-stroke: 2px var(--paper);
    text-shadow: 0 0 6px rgba(255,255,255,.9);
    letter-spacing: 4px;
  }
  .cup-name .cup-word { font-size: 80px; letter-spacing: 2px; }
  .format {
    left: 48px;
    top: 252px;
    font-family: "Tinos", serif;
    font-size: 90px;
    line-height: 1;
    color: var(--ink);
    text-shadow: 0 0 6px #fff, 0 0 3px #fff;
  }
  .format-sub {
    position: absolute;
    left: 514px;
    top: 246px;
    font-family: "Tinos", serif;
    font-size: 38px;
    line-height: 1.08;
    color: var(--ink);
    text-shadow: 0 0 5px #fff;
    margin: 0;
  }
  .when {
    position: absolute;
    left: 62px;
    top: 352px;
    margin: 0;
    font-family: "Nunito", sans-serif;
    font-weight: 900;
    font-size: 56px;
    line-height: 1.12;
    color: var(--paper);
    -webkit-text-stroke: 1.5px var(--ink);
    text-shadow: 2px 2px 0 var(--ink);
  }
  .when .date { letter-spacing: 2px; }
  .venue {
    position: absolute;
    left: 80px;
    top: 498px;
    width: 400px;
    margin: 0;
    text-align: center;
    font-family: "Tinos", serif;
    font-size: 20px;
    line-height: 1.5;
    color: var(--ink);
  }
  .entry {
    position: absolute;
    left: 20px;
    top: 660px;
    width: 350px;
    margin: 0;
    text-align: center;
    font-family: "Tinos", serif;
    font-size: 28px;
    line-height: 1.5;
    color: var(--ink);
  }
  .entry .fee {
    display: block;
    font-style: italic;
    font-weight: 700;
    color: var(--red);
    line-height: 1.4;
  }
  .entry .proceeds {
    display: block;
    line-height: 1.1;
  }
  .organisers {
    position: absolute;
    left: 632px;
    top: 782px;
    margin: 0;
    text-align: center;
    font-family: "Arimo", sans-serif;
    color: var(--ink);
    transform: rotate(-3deg);
  }
  .organisers .label { display: block; font-size: 27px; font-weight: 700; }
  .organisers .names { display: block; font-size: 19px; font-weight: 700; line-height: 1.35; margin-top: 6px; }
  .footer-text {
    position: absolute;
    left: 30px;
    top: 940px;
    width: 820px;
    transform: rotate(-3.5deg);
    transform-origin: left top;
    font-family: "Arimo", sans-serif;
  }
  .selection {
    margin: 0;
    font-size: 22px;
    font-weight: 700;
    line-height: 1.5;
    color: var(--paper);
  }
  .register {
    margin: 14px 0 0 108px;
    font-size: 40px;
    font-weight: 400;
    color: var(--red);
  }
  .contacts {
    margin: 16px 0 0 90px;
    font-size: 19px;
    color: var(--red);
    word-spacing: 2px;
  }
  .contacts .or { color: var(--paper); margin: 0 18px; }
</style>
</head>
<body>
<main class="flyer">
  <section class="panel">
    <svg class="art" width="878" height="1135" viewBox="0 0 878 1135">
      <defs>
        <linearGradient id="stadiumTone" x1="0" y1="0" x2="0.6" y2="1">
          <stop offset="0" stop-color="#2d3544"/>
          <stop offset="0.3" stop-color="#9aa5b2"/>
          <stop offset="0.55" stop-color="#eef1f3"/>
          <stop offset="1" stop-color="#ffffff"/>
        </linearGradient>
        <linearGradient id="flagTone" x1="0" y1="0" x2="0.2" y2="1">
          <stop offset="0" stop-color="#2f8a3c"/>
          <stop offset="0.38" stop-color="#3d9a48"/>
          <stop offset="0.48" stop-color="#f2f2f2"/>
          <stop offset="0.62" stop-color="#e8e8e8"/>
          <stop offset="0.72" stop-color="#d23a2e"/>
          <stop offset="1" stop-color="#b3261e"/>
        </linearGradient>
        <radialGradient id="ballTone" cx="0.45" cy="0.45" r="0.6">
          <stop offset="0" stop-color="#ffffff"/>
          <stop offset="0.5" stop-color="#7aa6e0"/>
          <stop offset="1" stop-color="#d5358e"/>
        </radialGradient>
        <linearGradient id="playerTone" x1="0" y1="0" x2="0" y2="1">
          <stop offset="0" stop-color="#3a3a3a"/>
          <stop offset="1" stop-color="#1b1b1b"/>
        </linearGradient>
      </defs>

      <rect width="878" height="760" fill="url(#stadiumTone)" role="img" aria-label="Floodlit football stadium background"/>
      <path d="M330 0 H878 V380 C760 330 600 300 470 230 C400 190 350 120 330 0 Z" fill="url(#flagTone)" opacity="0.85" role="img" aria-label="Waving Somaliland flag in green, white and red"/>

      <path d="M0 624 L150 610 L0 650 Z" fill="var(--red)"/>

      <path d="M600 340 C700 330 878 380 878 420 L878 735 L620 745 L595 900 L520 905 L470 700 L440 520 C450 430 520 350 600 340 Z" fill="url(#playerTone)" role="img" aria-label="Silhouette of a footballer kicking, with ink splatter"/>
      <circle cx="425" cy="810" r="64" fill="url(#ballTone)" role="img" aria-label="Colourful splashed football"/>

      <path d="M0 905 L878 880 V1135 H0 Z" fill="var(--band)"/>
    </svg>

    <h2 class="headline celebrating">Celebrating <span class="ordinal">23rd</span> <span class="occasion">Independence day</span></h2>
    <h1 class="headline cup-name">WARSADEQ <span class="cup-word">CUP</span></h1>
    <p class="headline format">11 ASIDE</p>
    <p class="format-sub">FOOTBALL<br>TOURNAMENT</p>
    <p class="when"><span class="date">10/05/2014</span><br>from 9am - 8pm</p>

    <p class="venue">Corvell Open Space, Tresham Lane,<br>Enfield, EN7 2QJ.<br>Refreshments, food and<br>entertainment will be provided.</p>

    <p class="entry">Spaces are limited and the
      <span class="fee">entry fee per team is<br>£200.</span>
      <span class="proceeds">All proceeds are for<br>charity projects in<br>Somaliland.</span>
    </p>

    <p class="organisers">
      <span class="label">Organised by</span>
      <span class="names">Dalmar FC and<br>Kindwell Foundation</span>
    </p>

    <div class="footer-text">
      <p class="selection">*The best players will have the opportunity to represent Somaliland<br>in an international game on the 17/05/2014.</p>
      <p class="register">To Register A Team Contact</p>
      <p class="contacts">Bashir Yusuf on 07591 248 613<span class="or">or</span>Warsame Hirsi on 07462 571 380.</p>
    </div>
  </section>
</main>
</body>
</html>
```